Business Card Design for Tarlo Cosmetics

hair extension supplier and mobile technican
make up and make up artistry
cosmetic eye contacts
eye lashes
general facial and hair products

```html
<!DOCTYPE html>
<html lang="en">
<head>
<meta charset="utf-8">
<title>Tarlo Cosmetics – Business Card</title>
<link href="https://fonts.googleapis.com/css2?family=Montserrat:wght@300;400&family=Open+Sans:wght@400&family=Pinyon+Script&display=swap" rel="stylesheet">
<style>
  :root {
    --page-bg: #eef3f8;
    --card-black: #050505;
    --ink-white: #ffffff;
    --ink-soft: #e6e6e6;
    --accent-grey: #9a9a9a;
    --tile-frame: #8c8c8c;
  }
  * { margin: 0; padding: 0; box-sizing: border-box; }
  html, body { width: 1200px; height: 900px; overflow: hidden; }
  body { background: var(--page-bg); position: relative; font-family: "Open Sans", Arial, sans-serif; }

  .card { position: absolute; background: var(--card-black); color: var(--ink-white); }

  /* Front */
  .card-front { left: 60px; top: 230px; width: 660px; height: 400px; }
  .wordmark { text-align: center; font-family: "Montserrat", Arial, sans-serif; font-weight: 300; color: var(--ink-white); }
  .card-front .wordmark { position: absolute; left: 0; right: 0; top: 95px; }
  .wordmark-main { display: block; font-size: 76px; letter-spacing: 26px; line-height: 1; padding-left: 26px; }
  .wordmark-sub { display: block; font-size: 24px; letter-spacing: 15px; margin-top: 10px; padding-left: 15px; }

  .contact-bar { position: absolute; left: 0; top: 305px; width: 9px; height: 70px; background: var(--accent-grey); }
  .contact-list { position: absolute; left: 26px; top: 292px; list-style: none; font-size: 13px; color: var(--ink-soft); }
  .contact-list li { display: flex; align-items: flex-start; gap: 8px; line-height: 1.5; margin-bottom: 3px; }
  .contact-list svg { width: 13px; height: 13px; flex: none; margin-top: 3px; fill: var(--ink-white); }
  .contact-list .at { width: 13px; flex: none; font-size: 14px; font-weight: 400; }

  .holder-name { position: absolute; right: 34px; top: 298px; font-family: "Pinyon Script", cursive; font-size: 28px; color: var(--ink-white); }
  .name-bar { position: absolute; right: 0; top: 292px; width: 12px; height: 42px; background: var(--ink-soft); }

  /* Back */
  .card-back { left: 795px; top: 165px; width: 320px; height: 500px; }
  .service-grid { position: absolute; left: 6px; top: 6px; width: 308px; height: 148px; display: grid; grid-template-columns: 1fr 1fr; grid-template-rows: 1fr 1fr; gap: 2px; border: 1px solid var(--tile-frame); background: var(--tile-frame); }
  .service-tile { position: relative; overflow: hidden; }
  .tile-hair { background: linear-gradient(120deg, #0d0d0d 35%, #6b3218 70%, #a5582d); }
  .tile-nails { background: linear-gradient(120deg, #111 40%, #4a4a4a 75%, #c9c2bc); }
  .tile-eyes { background: linear-gradient(120deg, #1a2a22 25%, #7a9c82 60%, #c7d8c9); }
  .tile-lashes { background: linear-gradient(110deg, #0b0b0b 45%, #5a3a1c 75%, #b6864c); }
  .tile-label { position: absolute; left: 8px; top: 6px; font-family: "Montserrat", Arial, sans-serif; font-weight: 300; color: var(--ink-white); line-height: 1; }
  .tile-label b { display: block; font-weight: 300; font-size: 15px; letter-spacing: 4px; }
  .tile-label span { display: block; font-size: 8px; letter-spacing: 2px; margin-top: 3px; }

  .about { position: absolute; left: 14px; right: 14px; top: 198px; text-align: center; font-family: "Montserrat", Arial, sans-serif; font-size: 10.5px; letter-spacing: 1.2px; line-height: 28px; color: var(--ink-soft); }
  .card-back .wordmark { position: absolute; left: 0; right: 0; top: 372px; }
  .card-back .wordmark-main { font-size: 50px; letter-spacing: 15px; padding-left: 15px; }
  .card-back .wordmark-sub { font-size: 16px; letter-spacing: 8px; padding-left: 8px; margin-top: 10px; }
</style>
</head>
<body>

<section class="card card-front" aria-label="Business card front">
  <h1 class="wordmark"><span class="wordmark-main">TARLO</span><span class="wordmark-sub">COSMETICS</span></h1>

  <div class="contact-bar"></div>
  <ul class="contact-list">
    <li><svg viewBox="0 0 16 16" aria-hidden="true"><path d="M8 1 0 8h2v7h4v-5h4v5h4V8h2z"/></svg><span>18 Larkspur st,<br>Northbridge, WA, 6003</span></li>
    <li><svg viewBox="0 0 16 16" aria-hidden="true"><path d="M4 0h8a1 1 0 0 1 1 1v14a1 1 0 0 1-1 1H4a1 1 0 0 1-1-1V1a1 1 0 0 1 1-1zm1 2v9h6V2zm3 10a1 1 0 1 0 0 2 1 1 0 0 0 0-2z"/></svg><span>0412 555 018</span></li>
    <li><span class="at">@</span><span>serena@tarlocosmetics.com.au</span></li>
    <li><svg viewBox="0 0 16 16" aria-hidden="true"><path d="M8 0a8 8 0 1 0 0 16A8 8 0 0 0 8 0zm5.9 7h-2.5a12 12 0 0 0-1-4.8A6 6 0 0 1 13.9 7zM8 2c.8 1 1.4 2.8 1.5 5h-3C6.6 4.8 7.2 3 8 2zM5.6 2.2A12 12 0 0 0 4.6 7H2.1a6 6 0 0 1 3.5-4.8zM2.1 9h2.5a12 12 0 0 0 1 4.8A6 6 0 0 1 2.1 9zM8 14c-.8-1-1.4-2.8-1.5-5h3c-.1 2.2-.7 4-1.5 5zm2.4-.2a12 12 0 0 0 1-4.8h2.5a6 6 0 0 1-3.5 4.8z"/></svg><span>www.tarlocosmetics.com.au</span></li>
  </ul>

  <p class="holder-name">Serena Vale</p>
  <div class="name-bar"></div>
</section>

<section class="card card-back" aria-label="Business card back">
  <div class="service-grid">
    <div class="service-tile tile-hair" role="img" aria-label="Photo of long flowing auburn hair">
      <p class="tile-label"><b>TARLO</b><span>HAIR</span></p>
    </div>
    <div class="service-tile tile-nails" role="img" aria-label="Photo of manicured nails on a hand">
      <p class="tile-label"><b>TARLO</b><span>NAILS</span></p>
    </div>
    <div class="service-tile tile-eyes" role="img" aria-label="Photo of a made-up eye with green contact lens">
      <p class="tile-label"><b>TARLO</b><span>EYES</span></p>
    </div>
    <div class="service-tile tile-lashes" role="img" aria-label="Close-up photo of an eye with long lashes">
      <p class="tile-label"><b>TARLO</b><span>LASHES</span></p>
    </div>
  </div>

  <p class="about">Tarlo Cosmetics is the company for my<br>businesses, Tarlo Hair, Tarlo Lashes,<br>Tarlo Nails &amp; Tarlo Eyes</p>

  <h2 class="wordmark"><span class="wordmark-main">TARLO</span><span class="wordmark-sub">COSMETICS</span></h2>
</section>

</body>
</html>
```